Copper Kettle Auctions business card design with existing logo

Looking for a sleek and sexy design using our current logo

Contact Information for Business Card

Name, address, email, phone, website. Marcus Delvane 482 Brambleton Road Suite 210C Marlow Bay OR 11907 Copperkettlebids.net (503)555-0174

```html
<!DOCTYPE html>
<html lang="en">
<head>
<meta charset="utf-8">
<title>Copper Kettle Auctions – Business Cards</title>
<link rel="stylesheet" href="https://fonts.googleapis.com/css2?family=Roboto:wght@400;700;900&display=swap">
<style>
  :root {
    --page: #1c1d20;
    --card: #2c2c2f;
    --card-shade: #242427;
    --red: #d8161d;
    --blue: #1c4fa0;
    --white: #f2f2f2;
    --text: #d9d9d9;
    --faint: #353539;
  }
  * { margin: 0; padding: 0; box-sizing: border-box; }
  html, body { width: 1200px; height: 2663px; overflow: hidden; }
  body {
    background: var(--page);
    font-family: "Roboto", Arial, sans-serif;
    color: var(--text);
  }
  .variant {
    height: 887.67px;
    display: flex;
    align-items: center;
    justify-content: center;
    gap: 40px;
    border-bottom: 1px solid #2a2b2f;
  }
  .variant:last-child { border-bottom: none; }
  .card {
    position: relative;
    width: 540px;
    height: 308px;
    border-radius: 18px;
    background: linear-gradient(160deg, var(--card) 0%, var(--card-shade) 100%);
    border: 4px solid var(--red);
    overflow: hidden;
  }
  .faint-mark {
    position: absolute;
    font-weight: 900;
    color: var(--faint);
    text-transform: uppercase;
    line-height: 0.95;
    z-index: 0;
  }
  .brand, .tagline, .contacts, .holder, .address, .back-brand, .corner-tab { z-index: 1; }

  /* front */
  .front .faint-mark { left: 30px; top: 196px; font-size: 42px; }
  .brand {
    position: absolute;
    left: 30px; top: 30px;
    display: flex; align-items: center; gap: 12px;
  }
  .brand-dot {
    width: 40px; height: 40px; border-radius: 50%;
    background: var(--blue);
  }
  .brand-name {
    font-weight: 900; font-size: 22px; letter-spacing: 1px;
    color: var(--red); text-transform: uppercase; line-height: 1.05;
  }
  .tagline {
    position: absolute; left: 82px; top: 84px;
    font-size: 11px; font-weight: 700; letter-spacing: 2.5px;
    color: var(--blue);
  }
  .contacts {
    position: absolute; left: 30px; top: 118px;
    list-style: none; font-size: 13px; line-height: 22px;
  }
  .contacts li { display: flex; align-items: center; gap: 8px; }
  .contacts svg { width: 12px; height: 12px; fill: var(--blue); }
  .holder {
    position: absolute; right: 40px; top: 34px;
    font-weight: 700; font-size: 22px; color: var(--white);
    text-transform: uppercase; letter-spacing: 0.5px;
  }
  .corner-tab {
    position: absolute; right: 0; top: 30px;
    width: 18px; height: 34px; background: var(--red);
  }
  .address {
    position: absolute; right: 40px; bottom: 34px;
    font-style: normal; text-align: right;
    font-size: 15px; line-height: 22px; color: var(--white);
  }

  /* back */
  .back .faint-mark { left: 30px; top: 30px; font-size: 80px; color: #38383c; }
  .back-brand {
    position: absolute; right: 34px; bottom: 30px; text-align: right;
  }
  .back-brand .brand-name { font-size: 24px; }
  .back-brand .tag {
    font-size: 11px; font-weight: 700; letter-spacing: 2.5px;
    color: var(--blue); margin-top: 4px;
  }
</style>
</head>
<body>

<section class="variant">
  <article class="card front">
    <div class="faint-mark">Copper<br>Kettle</div>
    <div class="brand"><span class="brand-dot"></span><span class="brand-name">Copper Kettle<br>Auctions</span></div>
    <div class="tagline">BUY·SELL·CONSIGN</div>
    <ul class="contacts">
      <li><svg viewBox="0 0 12 12"><path d="M2 1h3l1 3-2 1a7 7 0 0 0 3 3l1-2 3 1v3c-6 0-10-4-10-9z"/></svg>(503)555-0174</li>
      <li><svg viewBox="0 0 12 12"><circle cx="6" cy="6" r="5"/></svg>www.Copperkettlebids.net</li>
      <li><svg viewBox="0 0 12 12"><path d="M0 2h12v8H0z"/></svg>Marcus@Copperkettlebids.net</li>
    </ul>
    <h2 class="holder">Marcus Delvane</h2>
    <span class="corner-tab"></span>
    <address class="address">482 Brambleton Road<br>Suite 210C<br>Marlow Bay OR 11907</address>
  </article>
  <article class="card back">
    <div class="faint-mark">Copper<br>Kettle</div>
    <div class="back-brand"><div class="brand-name">Copper Kettle Auctions</div><div class="tag">BUY·SELL·CONSIGN</div></div>
  </article>
</section>

<section class="variant">
  <article class="card front">
    <div class="faint-mark">Copper<br>Kettle</div>
    <div class="brand"><span class="brand-dot"></span><span class="brand-name">Copper Kettle<br>Auctions</span></div>
    <div class="tagline">BUY·SELL·CONSIGN</div>
    <ul class="contacts">
      <li><svg viewBox="0 0 12 12"><path d="M2 1h3l1 3-2 1a7 7 0 0 0 3 3l1-2 3 1v3c-6 0-10-4-10-9z"/></svg>(503)555-0174</li>
      <li><svg viewBox="0 0 12 12"><circle cx="6" cy="6" r="5"/></svg>www.Copperkettlebids.net</li>
      <li><svg viewBox="0 0 12 12"><path d="M0 2h12v8H0z"/></svg>Tessa@Copperkettlebids.net</li>
    </ul>
    <h2 class="holder">Tessa Halloway</h2>
    <span class="corner-tab"></span>
    <address class="address">482 Brambleton Road<br>Suite 210C<br>Marlow Bay OR 11907</address>
  </article>
  <article class="card back">
    <div class="faint-mark">Copper<br>Kettle</div>
    <div class="back-brand"><div class="brand-name">Copper Kettle Auctions</div><div class="tag">BUY·SELL·CONSIGN</div></div>
  </article>
</section>

<section class="variant">
  <article class="card front">
    <div class="faint-mark">Copper<br>Kettle</div>
    <div class="brand"><span class="brand-dot"></span><span class="brand-name">Copper Kettle<br>Auctions</span></div>
    <div class="tagline">BUY·SELL·CONSIGN</div>
    <ul class="contacts">
      <li><svg viewBox="0 0 12 12"><path d="M2 1h3l1 3-2 1a7 7 0 0 0 3 3l1-2 3 1v3c-6 0-10-4-10-9z"/></svg>(503)555-0174</li>
      <li><svg viewBox="0 0 12 12"><circle cx="6" cy="6" r="5"/></svg>www.Copperkettlebids.net</li>
      <li><svg viewBox="0 0 12 12"><path d="M0 2h12v8H0z"/></svg>Rowan@Copperkettlebids.net</li>
    </ul>
    <h2 class="holder">Rowan Pike</h2>
    <span class="corner-tab"></span>
    <address class="address">482 Brambleton Road<br>Suite 210C<br>Marlow Bay OR 11907</address>
  </article>
  <article class="card back">
    <div class="faint-mark">Copper<br>Kettle</div>
    <div class="back-brand"><div class="brand-name">Copper Kettle Auctions</div><div class="tag">BUY·SELL·CONSIGN</div></div>
  </article>
</section>

</body>
</html>
```